Rw building ventures pty ltd

This is a development and construction company. Website can be set up on our domain rwbuildworks.net if we could change the domain to rwbuildworks.com.au would be great

Want the page to have eye catching designs, red, black and white are the preffered colours.

Check out www.toluqin.com.au it is my former company with my partner which i am now venturing out on my own, that is the perfect example of the website i want even allot of the information would be the same

Industry/Entity Type

Construction

Coding

Coded - Design and coding required

Number of Pages Required

5+ page

Requirements
Must have
• Company logo eye catching designs

```html
<!DOCTYPE html>
<html lang="en">
<head>
<meta charset="utf-8">
<title>RW Buildworks – Home</title>
<link rel="stylesheet" href="https://fonts.googleapis.com/css2?family=Lato:wght@300;400;700&display=swap">
<style>
:root{
  --red:#e8402a;
  --black:#000;
  --ink:#111;
  --white:#fff;
  --grey-bg:#efefef;
  --muted:#8a8a8a;
  --pink:#f6c3bb;
}
*{margin:0;padding:0;box-sizing:border-box}
html,body{width:1200px;height:1200px;overflow:hidden;background:var(--white);font-family:'Lato',sans-serif}
.stage{position:absolute;left:0;top:0;width:1932px;height:1932px;transform:scale(.62112);transform-origin:0 0}
.page{position:absolute;left:767px;top:0;width:398px;height:1932px;background:var(--white);overflow:hidden;color:var(--ink)}
.abs{position:absolute}
.bg-shapes{position:absolute;left:0;top:0}
.photo{position:absolute}
.eyebrow{position:absolute;font-size:3px;letter-spacing:.8px;color:var(--red);font-weight:700;text-transform:uppercase}
.heading{position:absolute;font-weight:400;line-height:1.2}
.dot{color:var(--red)}
.body-copy{position:absolute;font-size:3.6px;line-height:2.1;color:var(--muted)}
.btn{position:absolute;background:var(--red);color:var(--white);font-size:3.6px;display:flex;align-items:center;padding-left:12px;gap:8px;text-transform:uppercase}
.btn svg{width:10px;height:4px}
/* header */
.site-header .phone-icon{left:40px;top:12px;width:9px;height:9px;border-radius:50%;background:var(--red)}
.site-header .phone{left:54px;top:14px;font-size:3.6px;color:var(--white)}
.brand{position:absolute;color:var(--white);font-weight:700;font-size:6px;letter-spacing:.3px;text-transform:uppercase;display:flex;align-items:center;gap:3px}
.brand .mark{width:5px;height:5px;background:var(--red)}
.quote-btn{left:326px;top:12px;width:32px;height:8px;background:var(--red);color:var(--white);font-size:3px;display:flex;align-items:center;justify-content:center}
.nav{position:absolute;display:flex;font-size:3.2px;color:var(--white)}
.nav span{padding:0 6px;border-left:.5px solid #fff}
.nav span:first-child{border-left:none}
/* hero */
.hero{left:9px;top:43px;width:381px;height:212px;background:linear-gradient(160deg,#3a3530 0%,#2a2623 45%,#5a4332 75%,#7a5a3e 100%)}
.hero-title{left:39px;top:103px;font-size:15.5px;color:var(--white);line-height:1.15;font-weight:400}
/* cards */
.card-white{background:var(--white)}
.card-black{background:var(--black)}
.feature .bar{width:11px;height:1.5px;background:var(--red)}
.feature h4{font-size:4.4px;font-weight:400;margin-top:7px;color:var(--ink)}
.feature p{font-size:3.4px;line-height:2.2;color:var(--muted);margin-top:3px;width:74px}
/* portfolio */
.tile{position:absolute;background:linear-gradient(160deg,#4a4846,#2a2827)}
.tile .frame{position:absolute;left:7px;top:7px;right:7px;bottom:7px;border:.6px solid var(--red)}
.tile .label{position:absolute;color:var(--white);font-size:4.4px;display:flex;align-items:center;gap:4px}
.tile .label::before{content:"";position:absolute;left:0;top:-4px;width:9px;height:1.3px;background:var(--red)}
.tile .label svg{width:10px;height:4px}
/* testimonials */
.arrow-btn{position:absolute;top:1477px;width:25px;height:12px;background:var(--red);display:flex;align-items:center;justify-content:center}
.arrow-btn svg{width:10px;height:4px}
.t-card{position:absolute;top:1536px;width:101px;height:101px;background:var(--white);box-shadow:0 1px 4px rgba(0,0,0,.12)}
.t-card .q{position:absolute;right:14px;top:12px;font-size:30px;color:var(--pink);font-family:Georgia,serif;line-height:1}
.t-card p{position:absolute;left:14px;top:29px;width:68px;font-size:3.3px;line-height:2.2;color:var(--muted)}
.t-card .name{position:absolute;left:14px;top:74px;font-size:3.6px;color:var(--ink)}
.t-card .place{position:absolute;left:14px;top:82px;font-size:3.2px;color:#aaa}
/* form */
.field{position:absolute;width:101px;border-bottom:.6px solid #999;height:10px;font-size:3px;letter-spacing:.6px;color:#999;text-transform:uppercase}
.socials{position:absolute;left:321px;top:1875px;display:flex;gap:5px}
.socials span{width:9px;height:9px;border-radius:50%;background:var(--red)}
</style>
</head>
<body>
<div class="stage">
<main class="page">

  <svg class="bg-shapes" width="398" height="1932" viewBox="0 0 398 1932" aria-hidden="true">
    <defs>
      <linearGradient id="greyFade" x1="0" y1="0" x2="0" y2="1">
        <stop offset="0" stop-color="#ececec"/><stop offset="1" stop-color="#f6f6f6"/>
      </linearGradient>
    </defs>
    <polygon points="0,0 398,0 398,495 0,537" fill="#000"/>
    <polygon points="0,537 398,495 398,745 0,765" fill="url(#greyFade)"/>
    <polygon points="0,1160 398,1115 398,1380 0,1410" fill="#f1f1f1"/>
    <rect x="0" y="1455" width="398" height="150" fill="#000"/>
    <rect x="0" y="1851" width="398" height="81" fill="#000"/>
  </svg>

  <!-- header -->
  <header class="site-header">
    <div class="abs phone-icon"></div>
    <div class="abs phone">Call us: 0400 555 018</div>
    <div class="brand" style="left:175px;top:13px"><span class="mark"></span>RW Buildworks</div>
    <div class="abs quote-btn">GET A QUOTE</div>
    <nav class="nav" style="left:143px;top:31px"><span>About Us</span><span>Services</span><span>Projects</span><span>Contact Us</span></nav>
  </header>

  <!-- hero -->
  <section>
    <div class="photo hero" role="img" aria-label="Photo of a modern kitchen with marble island, bar stools and timber floor"></div>
    <h1 class="abs hero-title">Love The Home<br>You’re In<span class="dot">.</span></h1>
    <div class="btn" style="left:39px;top:151px;width:51px;height:11px;font-size:2.8px;padding-left:7px">View our projects</div>
  </section>

  <!-- what we do -->
  <section>
    <div class="photo" style="left:53px;top:291px;width:156px;height:141px;background:linear-gradient(150deg,#8a7a68,#4d3f33 55%,#b9ab98)" role="img" aria-label="Photo of a bathroom with freestanding bath and timber shutters"></div>
    <div class="abs card-white" style="left:190px;top:311px;width:155px;height:142px"></div>
    <div class="eyebrow" style="left:209px;top:331px">What we do</div>
    <h2 class="heading" style="left:209px;top:341px;font-size:12px">If you can dream<br>it, we can build it<span class="dot">.</span></h2>
    <p class="body-copy" style="left:209px;top:376px;width:120px">We plan, design and build homes and renovations across the city, managing every trade and detail from first sketch to final handover so your project runs smoothly and finishes on time.</p>
    <div class="btn" style="left:190px;top:434px;width:86px;height:19px">View our projects <svg viewBox="0 0 10 4"><path d="M0 2h9M7 .5 9.5 2 7 3.5" stroke="#fff" stroke-width=".5" fill="none"/></svg></div>
  </section>

  <!-- why choose us -->
  <section>
    <div class="eyebrow" style="left:39px;top:557px">Why choose us</div>
    <h2 class="heading" style="left:39px;top:566px;font-size:10.5px;width:160px">We take pride in our creed that a job isn’t finished until our client is absolutely satisfied<span class="dot">.</span></h2>
    <div class="abs feature" style="left:39px;top:623px"><div class="bar"></div><h4>Professionalism &amp; Expertise</h4><p>Licensed builders with decades of hands-on site experience.</p></div>
    <div class="abs feature" style="left:121px;top:623px"><div class="bar"></div><h4>Great Communication</h4><p>Clear updates at every stage, so nothing catches you out.</p></div>
    <div class="abs feature" style="left:39px;top:675px"><div class="bar"></div><h4>Timely</h4><p>Schedules we set, and schedules we keep, every single build.</p></div>
    <div class="abs feature" style="left:121px;top:675px"><div class="bar"></div><h4>Respectable</h4><p>Clean sites, courteous crews and care for your property.</p></div>
    <div class="photo" style="left:230px;top:605px;width:128px;height:160px;background:linear-gradient(180deg,#cfcac4,#a9a29a 60%,#6e6862);box-shadow:0 1px 4px rgba(0,0,0,.15)" role="img" aria-label="Photo of a floating timber staircase above a dining table"></div>
  </section>

  <!-- about -->
  <section>
    <div class="photo" style="left:39px;top:810px;width:175px;height:141px;background:linear-gradient(170deg,#d9cdd4,#6d4a44 45%,#3a2a22)" role="img" aria-label="Photo of a modern two-storey brick house at dusk"></div>
    <div class="abs card-black" style="left:197px;top:840px;width:161px;height:188px"></div>
    <div class="eyebrow" style="left:219px;top:861px">About us</div>
    <h2 class="heading" style="left:219px;top:870px;font-size:10.5px;color:#fff">At RW Buildworks<br>quality counts<span class="dot">.</span></h2>
    <p class="body-copy" style="left:219px;top:906px;width:118px;color:#fff">Every home we build starts with listening. We take the time to understand how you live, then shape each room, finish and fixture around it with honest advice and fair pricing.</p>
    <p class="body-copy" style="left:219px;top:949px;width:118px;color:#fff">Our team of carpenters, project managers and trusted trades share one standard: work we would be proud to live in ourselves. That care shows in every joint, surface and final detail.</p>
    <div class="btn" style="left:197px;top:1010px;width:87px;height:18px">Learn more <svg viewBox="0 0 10 4"><path d="M0 2h9M7 .5 9.5 2 7 3.5" stroke="#fff" stroke-width=".5" fill="none"/></svg></div>
  </section>

  <!-- portfolio -->
  <section>
    <h2 class="heading" style="left:190px;top:1071px;font-size:10.5px;width:172px">Take a look through our portfolio to see the craftsmanship &amp; personal detail into the work we do<span class="dot">.</span></h2>
    <div class="tile" style="left:39px;top:1114px;width:128px;height:143px" role="img" aria-label="Photo of a dark modern bedroom">
      <div class="frame"></div><div class="label" style="left:12px;top:124px">Bedrooms <svg viewBox="0 0 10 4"><path d="M0 2h9M7 .5 9.5 2 7 3.5" stroke="#fff" stroke-width=".5" fill="none"/></svg></div>
    </div>
    <div class="tile" style="left:176px;top:1151px;width:183px;height:106px" role="img" aria-label="Photo of an open living space">
      <div class="frame"></div><div class="label" style="left:13px;top:87px">Living Space <svg viewBox="0 0 10 4"><path d="M0 2h9M7 .5 9.5 2 7 3.5" stroke="#fff" stroke-width=".5" fill="none"/></svg></div>
    </div>
    <div class="tile" style="left:39px;top:1267px;width:183px;height:105px" role="img" aria-label="Photo of a dark modern bathroom">
      <div class="frame"></div><div class="label" style="left:127px;top:87px">Bathrooms <svg viewBox="0 0 10 4"><path d="M0 2h9M7 .5 9.5 2 7 3.5" stroke="#fff" stroke-width=".5" fill="none"/></svg></div>
    </div>
    <div class="tile" style="left:230px;top:1267px;width:129px;height:143px" role="img" aria-label="Photo of a kitchen with timber dining table">
      <div class="frame"></div><div class="label" style="left:78px;top:124px">Kitchens <svg viewBox="0 0 10 4"><path d="M0 2h9M7 .5 9.5 2 7 3.5" stroke="#fff" stroke-width=".5" fill="none"/></svg></div>
    </div>
  </section>

  <!-- testimonials -->
  <section>
    <div class="eyebrow" style="left:39px;top:1476px">Testimonials</div>
    <h2 class="heading" style="left:39px;top:1486px;font-size:10.5px;color:#fff">Don’t take our word for it. See what<br>others have to say about us<span class="dot">.</span></h2>
    <div class="arrow-btn" style="left:302px"><svg viewBox="0 0 10 4"><path d="M10 2H1M3 .5.5 2 3 3.5" stroke="#fff" stroke-width=".5" fill="none"/></svg></div>
    <div class="arrow-btn" style="left:333px"><svg viewBox="0 0 10 4"><path d="M0 2h9M7 .5 9.5 2 7 3.5" stroke="#fff" stroke-width=".5" fill="none"/></svg></div>
    <div class="t-card" style="left:39px"><span class="q">”</span><p>“We had a really good experience with them. They were awesome and everything has worked out great. We’re really happy with the house. I’d give them an A+”</p><div class="name">Kurt Lindqvist</div><div class="place">Melbourne</div></div>
    <div class="t-card" style="left:148px"><span class="q">”</span><p>We have been working with this home builder and the experience has been excellent. We highly recommend them for your next home project!</p><div class="name">Dale Horvat</div><div class="place">Southbank</div></div>
    <div class="t-card" style="left:257px"><span class="q">”</span><p>The price was great, the work was done in good time and to a high standard. The staff are friendly guys and take an interest in your ideas for your home.</p><div class="name">Noel Brandt</div><div class="place">Brunswick</div></div>
    <div class="t-card" style="left:366px"><span class="q">”</span><p>“We had a really good experience with them. They were awesome and everything has worked out great. We’re really happy with the house.”</p><div class="name">Kurt Lindqvist</div><div class="place">Melbourne</div></div>
  </section>

  <!-- contact -->
  <section>
    <h2 class="heading" style="left:0;width:398px;top:1689px;font-size:10.5px;text-align:center">Ready to get started?<br>Let us turn your vision into a reality<span class="dot">.</span></h2>
    <div class="field" style="left:78px;top:1737px">First name</div>
    <div class="field" style="left:215px;top:1737px">Last name</div>
    <div class="field" style="left:78px;top:1760px">Email</div>
    <div class="field" style="left:215px;top:1760px">Phone</div>
    <div class="btn" style="left:172px;top:1795px;width:53px;height:12px;padding-left:14px">Send <svg viewBox="0 0 10 4"><path d="M0 2h9M7 .5 9.5 2 7 3.5" stroke="#fff" stroke-width=".5" fill="none"/></svg></div>
  </section>

  <!-- footer -->
  <footer>
    <div class="brand" style="left:39px;top:1877px"><span class="mark"></span>RW Buildworks</div>
    <nav class="nav" style="left:143px;top:1878px"><span>About Us</span><span>Services</span><span>Projects</span><span>Contact Us</span></nav>
    <div class="socials"><span></span><span></span><span></span></div>
    <div class="abs" style="left:39px;top:1911px;width:319px;height:.6px;background:#444"></div>
    <div class="abs" style="left:0;width:398px;top:1927px;text-align:center;font-size:2.6px;color:#bbb">© 2024 RW Buildworks. All Rights Reserved.</div>
  </footer>

</main>
</div>
</body>
</html>
```